Tarnwell Signalworks Ltd

I need a website that is an informational only. We are a construction business building telecommunications sites. Seeing how our company is Tarnwell the color blue might want to be incorporated in the color scheme.
I can provide more picture of towers and wireless communications if needed.
current website www.tarnwellsignal.ca

Industry/Entity Type

Wireless Telecommunications, Construction

Coding

Coded - Design and coding required

Number of Pages Required

2 page

Font styles to use
Sans Serif

Colors

Designer to choose colors to be used in the design.

```html
<!DOCTYPE html>
<html lang="en">
<head>
<meta charset="utf-8">
<title>Tarnwell Signalworks Ltd</title>
<link href="https://fonts.googleapis.com/css2?family=Jost:wght@300;400;500&family=Montserrat:wght@400;500;600&display=swap" rel="stylesheet">
<style>
:root{
  --sky-top:#45598a;
  --sky-bottom:#6f86ad;
  --navy:#263760;
  --navy-deep:#1f2d57;
  --accent:#5aaee6;
  --ink:#2b2b2b;
  --muted:#555c66;
  --pale:#eef4f9;
  --page:#f7fafc;
  --white:#ffffff;
  --line:#e3e8ee;
}
*{box-sizing:border-box;margin:0;padding:0}
html,body{width:1200px;height:3582px;overflow:hidden}
body{position:relative;background:var(--page);font-family:'Montserrat',sans-serif;color:var(--ink)}
.abs{position:absolute}
.heading{font-family:'Jost',sans-serif;font-weight:400}

/* hero */
.hero{left:0;top:0;width:1200px;height:730px;background:linear-gradient(180deg,var(--sky-top),var(--sky-bottom))}
.hero-wave{left:0;top:600px}
.logo-box{left:72px;top:26px;width:158px;height:154px}
.logo-name{left:90px;top:70px;font-family:'Jost',sans-serif;font-size:30px;font-weight:400;color:var(--accent)}
.nav{top:52px;font-size:13px;color:var(--white)}
.nav-active{border-bottom:2px solid var(--white);padding-bottom:10px}
.btn{display:flex;align-items:center;justify-content:center;background:var(--accent);color:var(--white);border-radius:22px;font-size:13px;font-weight:500}
.hero-title{left:110px;top:312px;font-size:34px;line-height:42px;color:var(--white);font-weight:300}
.hero-sub{left:112px;top:405px;font-size:13px;line-height:18px;color:var(--white)}

/* intro */
.section-title{width:1200px;left:0;text-align:center;font-size:34px;color:var(--ink)}
.intro-text{left:255px;width:690px;text-align:center;font-size:12.5px;line-height:18px;color:var(--muted)}
.check{display:flex;gap:8px;font-size:12.5px;line-height:18px;color:var(--muted)}
.check svg{flex:none;margin-top:2px}

/* services */
.services{left:0;top:1228px;width:1200px;height:720px;background:var(--pale)}
.card{top:1371px;width:334px;height:444px;background:var(--white)}
.card-photo{left:0;top:0;width:334px;height:242px}
.card-icon{left:131px;top:206px;width:72px;height:72px;border-radius:50%;background:var(--white);display:flex;align-items:center;justify-content:center}
.card-title{left:0;width:334px;top:278px;text-align:center;font-family:'Jost',sans-serif;font-size:18px}
.card-rule{left:147px;top:308px;width:40px;height:2px;background:var(--navy)}
.card-text{left:28px;width:278px;top:320px;text-align:center;font-size:12.5px;line-height:18px;color:var(--muted)}
.card-dark .card-title,.card-dark .card-text{color:var(--white)}
.card-dark .card-rule{background:var(--white)}

/* about */
.about-panel{left:74px;top:2086px;width:640px;height:392px}
.about-text{left:110px;width:400px;font-size:13px;line-height:18px;color:var(--muted)}

/* contact */
.map{left:110px;top:2648px;width:461px;height:344px;background:var(--white);padding:10px}
.map-fill{width:100%;height:100%;background:linear-gradient(135deg,#c9ced3,#dfe3e6 55%,#c3c9ce)}
.field{background:var(--white);border:1px solid var(--line);font-size:12.5px;color:var(--muted);padding:12px 14px}

/* footer */
.footer{left:0;top:3122px;width:1200px;height:396px;background:linear-gradient(60deg,#2f4688 0%,#3e66a8 45%,#6aaee0 100%)}
.foot-head{font-size:16px;font-weight:600;color:var(--white)}
.foot-rule{height:2px;width:48px;background:var(--white)}
.foot-item{font-size:12.5px;color:var(--white);display:flex;gap:10px;align-items:center}
.social{width:36px;height:36px;border-radius:50%;background:var(--white)}
.copyright{left:0;top:3530px;width:1200px;text-align:center;font-size:12px;color:var(--ink)}
.copyright b{color:var(--navy-deep)}
</style>
</head>
<body>

<!-- HERO -->
<div class="abs hero" role="img" aria-label="Photo of a telecom lattice tower with antennas and a microwave dish against a blue sky"></div>
<svg class="abs hero-wave" width="1200" height="135" viewBox="0 0 1200 135">
  <path d="M0 42 C250 110 430 130 600 125 C850 118 1050 60 1200 18 L1200 135 L0 135 Z" fill="var(--navy-deep)"/>
  <path d="M0 42 C250 110 430 135 600 130 C850 124 1050 80 1200 40 L1200 135 L0 135 Z" fill="var(--page)"/>
  <path d="M592 104 l8 7 8-7 M592 112 l8 7 8-7" stroke="var(--accent)" stroke-width="2" fill="none"/>
</svg>

<svg class="abs logo-box" viewBox="0 0 158 154"><path d="M0 0 H158 V108 L0 154 Z" fill="var(--white)"/></svg>
<div class="abs logo-name">Tarnwell</div>

<svg class="abs" style="left:452px;top:28px" width="18" height="16" viewBox="0 0 18 16"><circle cx="3" cy="8" r="2" fill="var(--accent)"/><path d="M7 4 a5 5 0 0 1 0 8 M10 1 a9 9 0 0 1 0 14" stroke="var(--accent)" stroke-width="1.5" fill="none"/></svg>
<div class="abs nav nav-active" style="left:440px">Home</div>
<div class="abs nav" style="left:525px">About us</div>
<div class="abs nav" style="left:628px">Our Services</div>
<div class="abs nav" style="left:750px">Contact us</div>
<div class="abs btn" style="left:988px;top:40px;width:136px;height:38px">Get A Quote</div>

<svg class="abs" style="left:1120px;top:350px" width="30" height="60" viewBox="0 0 30 60"><circle cx="4" cy="4" r="2" fill="#c7d0de"/><circle cx="4" cy="20" r="3" fill="var(--white)"/><path d="M10 14 a7 7 0 0 1 0 12 M14 10 a12 12 0 0 1 0 20" stroke="var(--white)" stroke-width="2" fill="none"/><circle cx="4" cy="36" r="2" fill="#c7d0de"/><circle cx="4" cy="52" r="2" fill="#c7d0de"/></svg>

<div class="abs heading hero-title">Tarnwell Signalworks<br>Ltd</div>
<div class="abs hero-sub">we are dedicated to providing our customers<br>with friendly professional service...</div>
<div class="abs btn" style="left:112px;top:459px;width:155px;height:39px">Read More</div>

<!-- INTRO -->
<div class="abs heading section-title" style="top:835px">Tarnwell Signalworks Ltd</div>
<p class="abs intro-text" style="top:912px">Safety is number one.&nbsp; Tarnwell Ltd is committed to a strong safety policy, protecting its staff and the general public from accidents and harm.&nbsp; All Tarnwell Employees are certified “Tower Competent Climber and Rescue”.</p>
<p class="abs intro-text" style="top:985px">In addition to tower safety and fall protection Tarnwell’s safety training and practices<br>include but are not limited to the following:</p>

<svg width="0" height="0" style="position:absolute"><symbol id="tick" viewBox="0 0 14 14"><circle cx="7" cy="7" r="5.8" fill="none" stroke="var(--accent)" stroke-width="1.3"/><path d="M4.2 7.2 l2 2 4-4.4" fill="none" stroke="var(--accent)" stroke-width="1.4"/></symbol></svg>
<div class="abs check" style="left:221px;top:1060px"><svg width="14" height="14"><use href="#tick"/></svg>COR Certified</div>
<div class="abs check" style="left:367px;top:1060px"><svg width="14" height="14"><use href="#tick"/></svg>COR Certified</div>
<div class="abs check" style="left:497px;top:1060px"><svg width="14" height="14"><use href="#tick"/></svg>BC Level 1 first aid</div>
<div class="abs check" style="left:657px;top:1060px"><svg width="14" height="14"><use href="#tick"/></svg>Sprat Level 1</div>
<div class="abs check" style="left:800px;top:1060px"><svg width="14" height="14"><use href="#tick"/></svg>Monthly in office safety meetings</div>
<div class="abs check" style="left:334px;top:1105px"><svg width="14" height="14"><use href="#tick"/></svg>On site tailboard meeting with daily<br>Checklist sign off and picture documentation</div>
<div class="abs check" style="left:673px;top:1105px"><svg width="14" height="14"><use href="#tick"/></svg>Job site specific hazard assessment<br>and reporting</div>

<!-- SERVICES -->
<div class="abs services"></div>
<div class="abs heading section-title" style="top:1294px">Our Service</div>

<div class="abs card" style="left:74px">
  <div class="abs card-photo" role="img" aria-label="Photo of rooftop antenna equipment overlooking mountains" style="background:linear-gradient(180deg,#4a7fc4 0%,#8fb2d6 45%,#9a9a95 70%,#7d7f80 100%)"></div>
  <div class="abs card-icon"><svg width="40" height="40" viewBox="0 0 40 40" fill="none" stroke="#222" stroke-width="1.4"><rect x="5" y="14" width="14" height="22"/><rect x="19" y="22" width="16" height="14"/><path d="M9 19h2M13 19h2M9 24h2M13 24h2M9 29h2M13 29h2M23 27h3M29 27h3"/><path d="M27 22 L27 6 M24 12 L30 12 M23 22 L27 8 L31 22"/></svg></div>
  <div class="abs card-title">Rooftop Sites</div>
  <div class="abs card-rule"></div>
  <p class="abs card-text">Structural upgrades or simple ballast mounts. Shelter on the ground, leasehold build outs or cabinets on the roof.&nbsp; Tarnwell can install what you need where you need it.</p>
</div>

<svg class="abs" style="left:433px;top:1371px" width="334" height="470" viewBox="0 0 334 470"><path d="M0 0 H334 V446 L0 470 Z" fill="var(--navy)"/></svg>
<div class="abs card card-dark" style="left:433px;background:transparent">
  <div class="abs card-photo" role="img" aria-label="Photo of a lattice tower with antennas and dish against a blue sky" style="background:linear-gradient(180deg,#3e5787,#6b83aa)"></div>
  <div class="abs card-icon" style="background:var(--navy)"><svg width="40" height="40" viewBox="0 0 40 40" fill="none" stroke="#fff" stroke-width="1.4"><circle cx="20" cy="12" r="2"/><path d="M15 8 a6 6 0 0 0 0 8 M25 8 a6 6 0 0 1 0 8 M11 5 a11 11 0 0 0 0 14 M29 5 a11 11 0 0 1 0 14"/><path d="M20 14 L12 36 M20 14 L28 36 M15 28 H25 M10 36 H30"/></svg></div>
  <div class="abs card-title">Towers and Monopoles</div>
  <div class="abs card-rule"></div>
  <p class="abs card-text">Tarnwell can engineer, supply and install all your tower needs.&nbsp; New structures or existing, call us for pricing we would be happy to help out.</p>
</div>

<div class="abs card" style="left:790px">
  <div class="abs card-photo" role="img" aria-label="Photo of a forest construction site with concrete footings and mountains" style="background:linear-gradient(180deg,#9fb7d2 0%,#6f8a5a 40%,#4f6a3c 65%,#7c7468 100%)"></div>
  <div class="abs card-icon"><svg width="40" height="40" viewBox="0 0 40 40" fill="none" stroke="#222" stroke-width="1.4"><circle cx="20" cy="10" r="2"/><path d="M15 6 a6 6 0 0 0 0 8 M25 6 a6 6 0 0 1 0 8 M11 3 a11 11 0 0 0 0 14 M29 3 a11 11 0 0 1 0 14"/><path d="M20 12 L14 36 M20 12 L26 36 M16 26 H24 M17 20 H23 M12 36 H28"/></svg></div>
  <div class="abs card-title">In Building</div>
  <div class="abs card-rule"></div>
  <p class="abs card-text">Small office or large Hotel.&nbsp; Tarnwell has installed services into all size buildings. Fiber, cat6, or coax, we have the abilities to install, test, and get the job done.</p>
</div>

<!-- ABOUT -->
<svg class="abs" style="left:460px;top:2050px" width="664" height="465" viewBox="0 0 664 465" role="img" aria-label="Photo of a monopole tower on a snowy mountaintop above the clouds">
  <defs><linearGradient id="aboutSky" x1="0" y1="0" x2="0" y2="1"><stop offset="0" stop-color="#6d9fd8"/><stop offset=".55" stop-color="#c6d6e6"/><stop offset="1" stop-color="#eef2f6"/></linearGradient></defs>
  <path d="M0 0 H664 V465 H255 Z" fill="url(#aboutSky)"/>
  <path d="M30 30 L272 465 H232 Z" fill="#dfe9f3"/>
</svg>
<svg class="abs about-panel" viewBox="0 0 640 392"><path d="M0 0 H420 L640 392 H0 Z" fill="var(--page)"/></svg>
<div class="abs heading" style="left:110px;top:2118px;font-size:36px;color:var(--ink)">About us</div>
<p class="abs about-text" style="top:2186px">At Tarnwell Ltd, we are dedicated to providing our customers with friendly professional service. We value your business. We have made it our mission to provide reliable products and services in our customer-driven approach.</p>
<p class="abs about-text" style="top:2281px">Our courteous, professional team is able to support a range of services to meet your requirements.</p>
<p class="abs about-text" style="top:2335px">To learn more about Tarnwell Ltd, and the products<br>and services<br>we can offer,</p>
<svg class="abs" style="left:60px;top:2398px" width="620" height="56" viewBox="0 0 620 56"><path d="M0 8 L14 0 V8 Z" fill="var(--navy)"/><path d="M0 8 H620 L600 56 H0 Z" fill="var(--accent)"/></svg>
<div class="abs heading" style="left:110px;top:2412px;font-size:24px;font-weight:300;color:var(--navy-deep)">PLEASE CALL US AT <span style="font-weight:400">1-604-555-0187.</span></div>

<!-- CONTACT -->
<div class="abs map"><div class="map-fill" role="img" aria-label="Street map of the Langley area with a location pin"></div></div>
<div class="abs heading" style="left:633px;top:2640px;font-size:30px;color:var(--ink)">Quick Contact</div>
<div class="abs field" style="left:633px;top:2696px;width:239px;height:41px">First Name*</div>
<div class="abs field" style="left:885px;top:2696px;width:239px;height:41px">Last Name*</div>
<div class="abs field" style="left:633px;top:2749px;width:239px;height:41px">Phone*</div>
<div class="abs field" style="left:885px;top:2749px;width:239px;height:41px">Email*</div>
<div class="abs field" style="left:633px;top:2802px;width:491px;height:136px">Message</div>
<div class="abs btn" style="left:634px;top:2970px;width:155px;height:40px">Send</div>

<!-- FOOTER -->
<div class="abs footer"></div>
<div class="abs heading" style="left:115px;top:3250px;font-size:44px;font-weight:300;color:var(--white)">Tarnwell</div>
<div class="abs social" style="left:113px;top:3365px"></div>
<div class="abs social" style="left:161px;top:3365px"></div>
<div class="abs social" style="left:210px;top:3365px"></div>
<div class="abs social" style="left:256px;top:3365px"></div>

<div class="abs foot-head" style="left:427px;top:3232px">QUICK LINKS</div>
<div class="abs foot-rule" style="left:427px;top:3258px"></div>
<div class="abs foot-item" style="left:427px;top:3288px">&gt;&nbsp; Home</div>
<div class="abs foot-item" style="left:427px;top:3315px">&gt;&nbsp; About us</div>
<div class="abs foot-item" style="left:427px;top:3342px">&gt;&nbsp; Our Services</div>
<div class="abs foot-item" style="left:427px;top:3369px">&gt;&nbsp; Contact us</div>

<div class="abs foot-head" style="left:603px;top:3232px">CONTACT DETAIL</div>
<div class="abs foot-rule" style="left:603px;top:3258px"></div>
<div class="abs foot-item" style="left:603px;top:3292px"><svg width="12" height="12" viewBox="0 0 12 12"><path d="M2 1 L4.5 1 L5.5 3.5 L4 4.8 C4.8 6.6 5.6 7.4 7.2 8 L8.5 6.5 L11 7.5 V10 C11 10.6 10.5 11 10 11 C5 10.6 1.4 7 1 2 C1 1.5 1.4 1 2 1Z" fill="#fff"/></svg>1-604-555-0187</div>
<div class="abs foot-item" style="left:603px;top:3330px;align-items:flex-start"><svg width="12" height="12" viewBox="0 0 12 12" style="margin-top:1px"><rect x="1" y="2.5" width="10" height="7" fill="#fff"/><path d="M1 2.5 L6 6.5 L11 2.5" stroke="#3e66a8" fill="none"/></svg><span style="margin-top:8px">info@tarnwellsignal.ca</span></div>
<div class="abs foot-item" style="left:603px;top:3380px;align-items:flex-start"><svg width="12" height="14" viewBox="0 0 12 14"><path d="M6 13 C2 8 1 6.5 1 5 a5 5 0 0 1 10 0 c0 1.5-1 3-5 8Z" fill="#fff"/><circle cx="6" cy="5" r="1.8" fill="#3e66a8"/></svg><span>4410 Ridgeline Ave Langley, BC<br><span style="line-height:24px">V2Y 0K7</span></span></div>

<div class="abs foot-head" style="left:878px;top:3232px">NEWSLETTER</div>
<div class="abs foot-rule" style="left:878px;top:3258px"></div>
<p class="abs" style="left:878px;top:3288px;width:250px;font-size:12px;line-height:22px;color:var(--white)">Lorem Ipsum is simply dummy text of the printing and typesetting industry.</p>
<div class="abs" style="left:877px;top:3348px;width:247px;height:32px;border-radius:16px;background:var(--white);font-size:12px;font-style:italic;color:var(--muted);padding:8px 20px">Email Address</div>
<div class="abs" style="left:877px;top:3388px;width:247px;height:32px;border-radius:16px;background:var(--navy-deep);font-size:12px;color:var(--white);display:flex;align-items:center;justify-content:center">SUBSCRIBE</div>

<div class="abs copyright">Copyright © 2022 <b>TARNWELL</b>, All Rights Reserved.</div>

</body>
</html>
```